General Contractors need a new Crisp updated Card Design

We need a new business card design for our company of 25 years based in Toronto call Holvaster Building Inc. : Our goal is to be the leading commercial contractors in Toronto by providing exceptional value to our clients. We work very hard to deliver professional, quality, service in conjunction with consistent price competitiveness to all of our clients on every single project.

Target Market(s)

Design & Build Clients

Industry/Entity Type

Construction Company

Contact Information for Business Card

Address:
18 North Tamlin Glen Road, Unit 57, Marbrook Vale, ON, K7T 2R9
Office: 905-218-5937

Holvasters Logo
Employee Job Description
Employee Cell Phone #
Employee Email
www.holvaster-example.com

Colors

Designer to choose colors to be used in the design.

Requirements
Must have
• Quote Company Saying:
• "Professional. Quality. Service."
Nice to have
• New Crisp up to date look. simple & fresh ( Not to Busy)
Should not have
• NO BLUE PRINTS ON THE BUSINESS CARDS

```html
<!DOCTYPE html>
<html lang="en">
<head>
<meta charset="utf-8">
<title>Holvaster Building Inc. – Business Card</title>
<link href="https://fonts.googleapis.com/css2?family=Open+Sans:wght@400;600&display=swap" rel="stylesheet">
<style>
  :root {
    --teal-deep: #0b4a44;
    --teal: #0f5f57;
    --teal-mid: #2f7d73;
    --sage: #a7c2b8;
    --sage-light: #c6d8d1;
    --silver: #e4e9e7;
    --ink: #1f2b29;
    --divider: #4d5e5b;
    --white: #ffffff;
    --stage: #e6e9e8;
  }
  * { box-sizing: border-box; margin: 0; padding: 0; }
  html, body { width: 1200px; height: 675px; overflow: hidden; }
  body {
    background: var(--stage);
    font-family: "Open Sans", Arial, sans-serif;
    position: relative;
  }
  .card {
    position: absolute;
    top: 189px;
    width: 520px;
    height: 297px;
    overflow: hidden;
    box-shadow: 0 6px 18px rgba(0,0,0,.22);
  }
  .card--front { left: 50px; background: var(--sage); }
  .card--back {
    left: 630px;
    background: linear-gradient(180deg, var(--sage) 0%, var(--sage-light) 22%, var(--silver) 42%, var(--teal-mid) 62%, var(--teal) 78%, var(--teal-deep) 100%);
  }

  /* Front */
  .brand-panel {
    position: absolute; left: 0; top: 0;
    width: 300px; height: 138px;
    background: var(--white);
    box-shadow: 4px 0 8px rgba(0,0,0,.18);
    z-index: 1;
  }
  .brand {
    position: absolute; left: 20px; top: 56px;
    display: flex; align-items: center; gap: 9px;
  }
  .brand__square { width: 24px; height: 24px; background: var(--teal); flex: none; }
  .brand__name {
    font-weight: 600; font-size: 15px; letter-spacing: .4px;
    color: var(--teal); line-height: 1; white-space: nowrap;
  }
  .motto-band {
    position: absolute; left: 0; top: 138px;
    width: 100%; height: 159px;
    background: linear-gradient(180deg, var(--teal) 0%, #d3dcd9 14%, #eef1f0 22%, #7fa79f 42%, var(--teal) 62%, #2a786e 82%, var(--teal-deep) 100%);
  }
  .motto {
    position: absolute; left: 20px; top: 26px;
    font-size: 10px; letter-spacing: 1.4px; color: var(--ink);
    white-space: nowrap;
  }
  .motto__divider { margin: 0 8px; color: var(--divider); }

  .contact-list {
    position: absolute; left: 286px; top: 18px;
    width: 234px; list-style: none; z-index: 2;
  }
  .contact {
    display: flex; align-items: center;
    height: 30px; margin-bottom: 8px;
    background: linear-gradient(90deg, var(--teal) 0%, #cfdad6 30%, #eef1f0 45%, #8fb0a8 72%, var(--teal) 100%);
    box-shadow: -3px 3px 6px rgba(0,0,0,.25);
  }
  .contact--address { height: 34px; }
  .contact__icon {
    width: 30px; height: 30px; flex: none;
    display: flex; align-items: center; justify-content: center;
  }
  .contact__icon svg { width: 14px; height: 14px; }
  .contact__text {
    flex: 1; text-align: right; padding-right: 10px;
    font-size: 9.5px; color: var(--ink); white-space: nowrap;
  }
  .contact--address .contact__text { font-size: 8.5px; line-height: 1.3; }
  .contact__line { display: block; }

  /* Back */
  .back-brand {
    position: absolute; left: 0; top: 92px; width: 100%;
    display: flex; flex-direction: column; align-items: center; gap: 10px;
  }
  .back-brand__mark { display: flex; align-items: center; gap: 12px; }
  .back-brand__square { width: 40px; height: 40px; background: var(--teal); }
  .back-brand__name { font-weight: 600; font-size: 22px; letter-spacing: .5px; color: var(--teal); white-space: nowrap; }
  .tagline { font-size: 17px; letter-spacing: 1px; color: var(--ink); }
</style>
</head>
<body>

<section class="card card--front" aria-label="Business card front">
  <div class="brand-panel">
    <div class="brand">
      <span class="brand__square"></span>
      <span class="brand__name">HOLVASTER BUILDING INC.</span>
    </div>
  </div>

  <div class="motto-band">
    <p class="motto">PROFESSIONAL<span class="motto__divider">|</span>QUALITY<span class="motto__divider">|</span>SERVICE</p>
  </div>

  <ul class="contact-list">
    <li class="contact contact--address">
      <span class="contact__icon">
        <svg viewBox="0 0 24 24"><path d="M12 2a7 7 0 0 0-7 7c0 5 7 13 7 13s7-8 7-13a7 7 0 0 0-7-7zm0 9.5A2.5 2.5 0 1 1 12 6.5a2.5 2.5 0 0 1 0 5z" fill="#0b4a44"/></svg>
      </span>
      <span class="contact__text">
        <span class="contact__line">18 North Tamlin Glen Road, Unit 57,</span>
        <span class="contact__line">Marbrook Vale, ON, K7T 2R9</span>
      </span>
    </li>
    <li class="contact">
      <span class="contact__icon">
        <svg viewBox="0 0 24 24" fill="none" stroke="#0b4a44" stroke-width="2"><circle cx="12" cy="12" r="9"/><path d="M3 12h18M12 3c3 3 3 15 0 18M12 3c-3 3-3 15 0 18"/></svg>
      </span>
      <span class="contact__text">http://www.holvaster-example.com</span>
    </li>
    <li class="contact">
      <span class="contact__icon">
        <svg viewBox="0 0 24 24"><rect x="2" y="5" width="20" height="14" fill="#0b4a44"/><path d="M2 5l10 8 10-8" fill="none" stroke="#cfdad6" stroke-width="1.6"/></svg>
      </span>
      <span class="contact__text">sh@holvaster-example.com</span>
    </li>
    <li class="contact">
      <span class="contact__icon">
        <svg viewBox="0 0 24 24"><path d="M6.6 10.8a15 15 0 0 0 6.6 6.6l2.2-2.2a1 1 0 0 1 1-.25 11 11 0 0 0 3.6.6 1 1 0 0 1 1 1V20a1 1 0 0 1-1 1A17 17 0 0 1 3 4a1 1 0 0 1 1-1h3.5a1 1 0 0 1 1 1c0 1.25.2 2.450.6 3.6a1 1 0 0 1-.25 1z" fill="#0b4a44"/></svg>
      </span>
      <span class="contact__text">905-218-5937</span>
    </li>
    <li class="contact">
      <span class="contact__icon">
        <svg viewBox="0 0 24 24"><rect x="7" y="2" width="10" height="20" rx="2" fill="#0b4a44"/><rect x="9" y="5" width="6" height="11" fill="#cfdad6"/></svg>
      </span>
      <span class="contact__text">416-555-0148</span>
    </li>
  </ul>
</section>

<section class="card card--back" aria-label="Business card back">
  <div class="back-brand">
    <div class="back-brand__mark">
      <span class="back-brand__square"></span>
      <span class="back-brand__name">HOLVASTER BUILDING INC.</span>
    </div>
    <p class="tagline">leading commercial contractors</p>
  </div>
</section>

</body>
</html>
```